Landing Page and Logo for Auto-Blogging Platform

I created a platform that allows users to start a blog for their business, hobby, charity, etc. I need a landing page where users can learn about the platform, benefits of consistent blogging, SEO value, plans/pricing, etc. The landing page needs to have multiple call to action buttons encouraging the visitor to register/sign up for a free trial.

In addition to the landing page, I need a page for users to establish the settings for their blog. This page should be a fairly simple form, intended for the user to enter a few details to set up their blog:
1. Name of Blog
2. Up to 10 topics and/or keywords the blog should focus on
3. Theme: Color-scheme and logo upload for blog.

I have attached the specifications of the platform's functionality so you can better understand how it works, plans/pricing, etc.

I also need a logo for the business. The name of the platform is PostNook.

Target Market(s)

Website owners, bloggers, business owners

Industry/Entity Type

Technology, Internet, web design

Coding

Coded - Design and coding required

Number of Pages Required

2 page

Colors
0054AA
0677BA
7BADD7
CADEEF
E8F1F8
0094D4
00A9DD
6FCCEA
C7EBF8
E9F6FB

Requirements
Must have
• Eye-catching design but fairly light on content (keep it simple and brief.)
Nice to have
• Eye-catching yet simple design, clean and easy to understand what we are offering.
Should not have
• Too much “wordy” and confusing content.

```html
<!DOCTYPE html>
<html lang="en">
<head>
<meta charset="utf-8">
<title>PostNook – Auto-Blogging Platform</title>
<link href="https://fonts.googleapis.com/css2?family=Poppins:wght@400;500;600;700&family=Quicksand:wght@500;600;700&display=swap" rel="stylesheet">
<style>
:root{
  --blue-deep:#0054AA;
  --blue-mid:#0677BA;
  --blue-bright:#0094D4;
  --blue-sky:#00A9DD;
  --blue-soft:#6FCCEA;
  --blue-pale:#C7EBF8;
  --blue-mist:#E9F6FB;
  --ink:#1b1b1b;
  --muted:#8a8a8a;
  --footer:#232323;
}
*{box-sizing:border-box;margin:0;padding:0}
html,body{width:1200px;height:3348px;overflow:hidden;background:#fff}
body{font-family:"Poppins",sans-serif;color:var(--ink);position:relative}
section,header,footer{position:relative;width:1200px;overflow:hidden}
.abs{position:absolute}
.title{font-family:"Quicksand",sans-serif;font-weight:600;font-size:26px;text-align:center;position:absolute;left:0;right:0}
.btn{position:absolute;display:flex;align-items:center;justify-content:center;color:#fff;font-size:12px;border-radius:2px;white-space:nowrap}
.btn-soft{background:var(--blue-soft)}
.btn-deep{background:var(--blue-deep)}

/* nav */
.site-nav{height:67px;background:#fff}
.brand{position:absolute;display:flex;align-items:center;gap:10px;font-weight:700;color:var(--blue-deep)}
.brand-mark{width:26px;height:26px;border:3px solid var(--blue-deep);border-radius:3px}
.nav-link{position:absolute;top:24px;font-size:12px;color:#444}
.nav-link.active{color:var(--blue-deep);text-decoration:underline}

/* hero */
.hero{height:502px}
.hero-photo{position:absolute;inset:0;background:linear-gradient(100deg,#2a211c 0%,#4a3a2e 35%,#8a5a34 60%,#c98a4c 75%,#3b2f29 100%)}
.hero-shade{position:absolute;inset:0;background:linear-gradient(90deg,rgba(0,0,0,.45),rgba(0,0,0,0) 60%)}
.hero h1{position:absolute;left:156px;top:138px;color:#fff;font-size:37px;line-height:47px;font-weight:700}

/* blogs */
.blogs{height:840px}
.blog-card{position:absolute;border-radius:12px;overflow:hidden}
.blog-photo{position:absolute;inset:0}
.blog-info{position:absolute;background:#fff;border-radius:10px 10px 0 0;padding:22px 18px 0}
.tag{position:absolute;top:-8px;left:18px;background:var(--blue-soft);color:#fff;font-size:9px;padding:2px 10px;border-radius:3px}
.meta{font-size:9px;color:var(--muted)}
.blog-title{font-size:13px;font-weight:500;line-height:16px;margin-top:4px;width:200px}
.go{position:absolute;right:22px;top:36px;width:24px;height:24px;border-radius:50%;display:flex;align-items:center;justify-content:center}

/* pricing */
.pricing{height:613px;background:linear-gradient(180deg,#0a6fc8 0%,#0b86d6 60%,#0a71c9 100%)}
.plan{position:absolute;top:146px;width:250px;height:301px;background:#fff;border-radius:6px;overflow:hidden;text-align:center}
.plan-head{height:50px;display:flex;align-items:center;justify-content:center;color:#fff;font-weight:600;font-size:16px;background:var(--blue-sky)}
.plan.featured .plan-head{background:var(--blue-deep)}
.plan.featured{box-shadow:0 0 0 2px #e6eefb}
.plan-icon{margin:30px auto 0;width:36px;height:36px}
.plan-text{font-size:10.5px;line-height:16px;margin-top:10px;padding:0 30px}
.plan-price{font-size:22px;font-weight:700;color:var(--blue-sky);margin-top:8px}
.plan .btn{left:75px;top:231px;width:100px;height:32px;font-size:11px}

/* steps */
.steps{height:504px}
.step-line{position:absolute;top:180px;width:4px;height:152px;background:linear-gradient(180deg,rgba(0,0,0,0),rgba(0,0,0,.07),rgba(0,0,0,0))}
.step{position:absolute;top:225px;display:flex;align-items:center;gap:18px}
.step-ring{width:62px;height:62px;border-radius:50%;background:#fff;box-shadow:0 6px 18px rgba(0,0,0,.12);display:flex;align-items:center;justify-content:center;flex:none}
.step-num{font-size:15px;color:var(--blue-pale);line-height:16px}
.step-name{font-size:13px;color:var(--blue-mid);font-weight:500;line-height:16px;white-space:nowrap}

/* faq */
.faq{height:549px;background:#fff}
.faq-item{position:absolute;left:200px;width:434px;border-bottom:1px solid #eee;font-size:12px;color:var(--blue-soft);padding-bottom:10px}
.faq-item.open .q{color:var(--blue-deep);font-weight:600}
.faq-item .ico{position:absolute;right:0;top:1px;width:15px;height:15px;border-radius:50%;background:var(--blue-soft);color:#fff;font-size:12px;line-height:14px;text-align:center}
.faq-item.open .ico{background:var(--blue-deep)}
.answer{color:#333;font-size:10px;line-height:17.5px;margin-top:12px}
.faq-photo{position:absolute;left:688px;top:147px;width:312px;height:301px;border-radius:30px;background:radial-gradient(circle at 40% 45%,#c79a62,#6c4a2d 60%,#231a14)}

/* footer */
.site-footer{height:273px;background:var(--footer);color:#ddd}
.foot-h{position:absolute;top:56px;font-size:12px;font-weight:600;color:var(--blue-soft)}
.foot-line{position:absolute;font-size:11px;display:flex;gap:8px;line-height:16px}
.quick{position:absolute;left:652px;top:84px;font-size:10px;line-height:18px}
.quick .active{color:var(--blue-soft);text-decoration:underline}
.pay{position:absolute;width:36px;height:14px;border-radius:3px;background:#555}
.bar{position:absolute;left:0;bottom:0;width:1200px;height:34px;background:var(--blue-deep);font-size:10px;color:#fff}
.social{position:absolute;top:9px;width:15px;height:15px;background:#fff;opacity:.9;border-radius:2px}
</style>
</head>
<body>

<header class="site-nav">
  <div class="brand" style="left:156px;top:18px;font-size:26px"><span class="brand-mark"></span>PostNook</div>
  <span class="nav-link active" style="left:602px">Home</span>
  <span class="nav-link" style="left:659px">Pricing</span>
  <span class="nav-link" style="left:718px">Blogs</span>
  <span class="nav-link" style="left:773px">About Us</span>
  <span class="nav-link" style="left:845px">FAQs</span>
  <span class="nav-link" style="left:900px">Support</span>
  <span class="btn" style="left:966px;top:18px;width:72px;height:30px;background:var(--blue-bright)">Sign In</span>
</header>

<section class="hero">
  <div class="hero-photo" role="img" aria-label="Hands typing on a laptop keyboard in warm window light"></div>
  <div class="hero-shade"></div>
  <h1>Ready With Your Blog<br>Post And Looking To Post<br>The Same!</h1>
  <span class="btn btn-deep" style="left:156px;top:305px;width:214px;height:35px">Signup For 14-Day Free Trial</span>
</section>

<section class="blogs">
  <article class="blog-card" style="left:156px;top:82px;width:430px;height:287px">
    <div class="blog-photo" role="img" aria-label="Person holding a phone with a glowing security shield graphic" style="background:linear-gradient(120deg,#1d2a36,#2f5f86 50%,#6b7d8c)"></div>
    <div class="blog-info" style="left:19px;top:206px;width:311px;height:81px">
      <span class="tag">Business</span>
      <p class="meta">Aug 13, 2024 &nbsp;•&nbsp; 4 Minutes</p>
      <p class="blog-title">Why AI Is Now Essential to API Security</p>
      <span class="go" style="background:var(--blue-soft)"><svg width="10" height="10" viewBox="0 0 10 10"><path d="M1 5h7M5 2l3 3-3 3" stroke="#fff" stroke-width="1.5" fill="none"/></svg></span>
    </div>
  </article>
  <article class="blog-card" style="left:156px;top:418px;width:430px;height:288px">
    <div class="blog-photo" role="img" aria-label="Children standing in a narrow village lane" style="background:linear-gradient(120deg,#3a3026,#6f5a44 50%,#8c7a5c)"></div>
    <div class="blog-info" style="left:19px;top:207px;width:311px;height:81px">
      <span class="tag">charity</span>
      <p class="meta">Aug 13, 2024 &nbsp;•&nbsp; 4 Minutes</p>
      <p class="blog-title">How best to give during a humanitarian crisis</p>
      <span class="go" style="background:var(--blue-soft)"><svg width="10" height="10" viewBox="0 0 10 10"><path d="M1 5h7M5 2l3 3-3 3" stroke="#fff" stroke-width="1.5" fill="none"/></svg></span>
    </div>
  </article>
  <h2 class="title" style="left:612px;right:156px;top:128px;font-size:24px">Our Blogs</h2>
  <article class="blog-card" style="left:612px;top:202px;width:432px;height:376px">
    <div class="blog-photo" role="img" aria-label="Laptop with a small shopping cart and charts on a desk" style="background:linear-gradient(130deg,#c9863f,#e9dccb 45%,#c5ccd6 75%,#9aa6b5)"></div>
    <div class="blog-info" style="left:21px;top:299px;width:311px;height:77px">
      <span class="tag">Business</span>
      <p class="meta">Aug 13, 2024 &nbsp;•&nbsp; 4 Minutes</p>
      <p class="blog-title">3 Inspiring social proof examples for eCommerce</p>
      <span class="go" style="background:var(--blue-deep)"><svg width="10" height="10" viewBox="0 0 10 10"><path d="M1 5h7M5 2l3 3-3 3" stroke="#fff" stroke-width="1.5" fill="none"/></svg></span>
    </div>
  </article>
  <span class="btn btn-soft" style="left:783px;top:630px;width:91px;height:30px;font-size:11px">View All</span>
</section>

<section class="pricing">
  <h2 class="title" style="top:72px;color:#fff;font-weight:500">SAAS Model PostNook Subscriptions Are Packages</h2>
  <div class="plan" style="left:200px">
    <div class="plan-head">Base Plan</div>
    <svg class="plan-icon" viewBox="0 0 24 24"><path d="M12 2l3 6.5 7 .8-5.2 4.8 1.5 7L12 17.5 5.7 21l1.5-7L2 9.3l7-.8z" fill="none" stroke="#aaa" stroke-width="1.2"/></svg>
    <p class="plan-text">1 Blog Post (Up To 2,000 Words)<br>Every Month:</p>
    <p class="plan-price">$9.99/Mo.</p>
    <span class="btn btn-soft">Get Started</span>
  </div>
  <div class="plan" style="left:475px">
    <div class="plan-head">Premium Plan</div>
    <svg class="plan-icon" viewBox="0 0 24 24"><path d="M12 21S3 14.5 3 8.5A4.5 4.5 0 0 1 12 6a4.5 4.5 0 0 1 9 2.5C21 14.5 12 21 12 21z" fill="none" stroke="#aaa" stroke-width="1.2"/></svg>
    <p class="plan-text">1 Blog Post (Up To 2,000 Words)<br>Every Week:</p>
    <p class="plan-price">$14.99/Mo.</p>
    <span class="btn btn-soft">Get Started</span>
  </div>
  <div class="plan featured" style="left:750px">
    <div class="plan-head">Ultimate Plan</div>
    <svg class="plan-icon" viewBox="0 0 24 24"><path d="M2 9l4-5h12l4 5-10 12zM2 9h20M9 4l3 5 3-5M12 9v12M6 4l3 5M18 4l-3 5" fill="none" stroke="#0054AA" stroke-width="1.2"/></svg>
    <p class="plan-text">1 Blog Post (Up To 3,000 Words) Per Day Plus Unlimited Manual &nbsp;Posting:</p>
    <p class="plan-price">$24.99/Mo.</p>
    <span class="btn btn-deep">Get Started</span>
  </div>
  <span class="btn btn-soft" style="left:492px;top:497px;width:214px;height:33px">Signup For 14-Day Free Trial</span>
</section>

<section class="steps">
  <h2 class="title" style="top:72px;font-weight:500">How PostNook Works?</h2>
  <span class="step-line" style="left:188px"></span>
  <span class="step-line" style="left:417px"></span>
  <span class="step-line" style="left:622px"></span>
  <span class="step-line" style="left:818px"></span>
  <div class="step" style="left:159px">
    <span class="step-ring"><svg width="26" height="26" viewBox="0 0 24 24" fill="none" stroke="#555" stroke-width="1.3"><circle cx="10" cy="8" r="4"/><path d="M3 20c0-4 3-6 7-6s5 1 6 2M18 14v6M15 17h6"/></svg></span>
    <div><p class="step-num">01</p><p class="step-name">Sign Up With Us</p></div>
  </div>
  <div class="step" style="left:388px">
    <span class="step-ring"><svg width="26" height="26" viewBox="0 0 24 24" fill="none" stroke="#555" stroke-width="1.3"><path d="M9 12V4a1.5 1.5 0 0 1 3 0v7M12 11V9a1.5 1.5 0 0 1 3 0v3M15 12v-1a1.5 1.5 0 0 1 3 0v5c0 3-2 6-6 6s-6-3-7-6l-1-3a1.5 1.5 0 0 1 3-1l2 2"/></svg></span>
    <div><p class="step-num">02</p><p class="step-name">Select Topic</p></div>
  </div>
  <div class="step" style="left:593px">
    <span class="step-ring"><svg width="26" height="26" viewBox="0 0 24 24" fill="none" stroke="#555" stroke-width="1.3"><rect x="3" y="5" width="15" height="15" rx="2"/><path d="M10 14l9-9 2 2-9 9-3 1z"/></svg></span>
    <div><p class="step-num">03</p><p class="step-name">Write Blog With<br>Help Of WriteMate AI</p></div>
  </div>
  <div class="step" style="left:789px">
    <span class="step-ring"><svg width="26" height="26" viewBox="0 0 24 24" fill="none" stroke="#555" stroke-width="1.3"><circle cx="12" cy="9" r="6"/><circle cx="12" cy="9" r="2.5"/><path d="M8 14l-3 6 3-1 2 3 2-6M16 14l3 6-3-1-2 3-2-6"/></svg></span>
    <div><p class="step-num">04</p><p class="step-name">Review And Submit</p></div>
  </div>
  <span class="btn btn-soft" style="left:492px;top:390px;width:214px;height:33px">Signup For 14-Day Free Trial</span>
</section>

<section class="faq">
  <h2 class="title" style="top:92px;font-weight:500">Frequently Asked Questions</h2>
  <div class="faq-item" style="top:155px"><p class="q">What is Lorem Ipsum?</p><span class="ico">+</span></div>
  <div class="faq-item open" style="top:199px"><p class="q">Why do we use it?</p><span class="ico">−</span>
    <p class="answer">It is a long established fact that a reader will be distracted by the readable content of a page when looking at its layout. The point of using Lorem Ipsum is that it has a more-or-less normal distribution of letters, as opposed to using 'Content here, content here', making it look like readable English. Many desktop publishing packages and web page editors now use Lorem...</p></div>
  <div class="faq-item" style="top:343px"><p class="q">Where does it come from?</p><span class="ico">+</span></div>
  <div class="faq-item" style="top:386px;border:none"><p class="q">Where can I get some?</p><span class="ico">+</span></div>
  <span class="btn btn-soft" style="left:200px;top:436px;width:91px;height:33px;font-size:11px">View All</span>
  <div class="faq-photo" role="img" aria-label="Wooden letter blocks spelling FAQ placed by a hand"></div>
</section>

<footer class="site-footer">
  <div class="brand" style="left:156px;top:58px;font-size:26px;color:#fff"><span class="brand-mark" style="border-color:#fff"></span>PostNook</div>
  <p class="abs" style="left:210px;top:118px;font-size:11px;color:var(--blue-soft)">We Accept:</p>
  <span class="pay" style="left:160px;top:145px"></span><span class="pay" style="left:208px;top:145px"></span><span class="pay" style="left:256px;top:145px"></span>
  <span class="pay" style="left:160px;top:166px"></span><span class="pay" style="left:208px;top:166px"></span><span class="pay" style="left:256px;top:166px"></span>

  <p class="foot-h" style="left:419px">Contact Us</p>
  <p class="foot-line" style="left:419px;top:84px"><svg width="10" height="12" viewBox="0 0 24 24"><path d="M5 3h4l2 5-3 2a11 11 0 0 0 6 6l2-3 5 2v4a2 2 0 0 1-2 2A17 17 0 0 1 3 5a2 2 0 0 1 2-2z" fill="#ccc"/></svg>+1300 555 017</p>
  <p class="foot-line" style="left:419px;top:116px"><svg width="10" height="12" viewBox="0 0 24 24"><path d="M2 6h20v13H2zM2 6l10 7 10-7" fill="none" stroke="#ccc" stroke-width="2"/></svg>hello@postnook.com</p>
  <p class="foot-line" style="left:419px;top:148px"><svg width="10" height="12" viewBox="0 0 24 24"><path d="M12 22s7-7 7-12a7 7 0 0 0-14 0c0 5 7 12 7 12z" fill="#ccc"/></svg>Lorem ipsum, 58 Harbour Lane,<br>Street, Australia</p>

  <p class="foot-h" style="left:652px">Quick Links</p>
  <div class="quick"><p class="active">Home</p><p>Pricing</p><p>Blogs</p><p>About Us</p><p>FAQs</p><p>Support</p></div>

  <svg class="abs" style="left:791px;top:52px" width="30" height="26" viewBox="0 0 30 26"><path d="M2 10L15 2l13 8v14H2z" fill="var(--blue-pale)"/><path d="M2 10l13 9 13-9" fill="none" stroke="#fff" stroke-width="1.5"/></svg>
  <p class="abs" style="left:830px;top:52px;font-size:11px;font-weight:600;color:var(--blue-soft)">Sign Up And Save!</p>
  <p class="abs" style="left:830px;top:68px;font-size:9px">Exclusive Email Offers &amp; Limited Time</p>
  <div class="abs" style="left:791px;top:99px;width:253px;height:30px;border:1px solid #444;font-size:9px;color:#888;padding:9px 12px">Enter Email</div>
  <span class="btn btn-soft" style="left:791px;top:144px;width:77px;height:28px;font-size:10px">Sign Up</span>

  <div class="bar">
    <p class="abs" style="left:156px;top:10px">Copyright © 2024 PostNook, All rights reserved</p>
    <span class="social" style="left:930px"></span>
    <span class="social" style="left:955px"></span>
    <span class="social" style="left:978px;top:6px;width:22px;height:22px;border-radius:50%;background:var(--blue-soft)"></span>
  </div>
</footer>

</body>
</html>
```